" Nosso escritório opera, assim, com setores departamentalizados para propiciar conhecimentos especializados, e, via de consequência, atendimentos especializados nos diversos setores do Direito. Foi por esta consciência que montamos uma equipe de caráter multidisciplinar, formada por profissionais com conhecimento específico e profundo nas suas respectivas áreas de atuação, voltado para advocacia empresarial. No âmbito da advocacia preventiva oferecemos aos nossos clientes, consultoria e assessoria permanente, a fim de mantê-los atualizados a respeito das possíveis implicações jurídicas em seus negócios, alertá-los quanto a possíveis oportunidades de benefícios e também, emitindo pareceres sobre diversos temas, a fim de ajudá-los nas tomadas de decisões. No mundo empresarial moderno as decisões são tomadas cada vez mais rápidas, contudo, para que o empresário tome decisões importantes de maneira eficaz, necessita sempre de um respaldo jurídico, pois, por mais simples que pareça a decisão a ser tomada, ela pode levar a empresa a uma série de implicações. No litígio, primamos pela solução amigável, ou extrajudicial, se alcançáveis, sempre condicionadas à fiel defesa dos interesses que nos confiaram. Já no âmbito contencioso, seja em sede de processo administrativo ou judicial, contamos com o dedicado trabalho de nossa equipe, sempre na procura das melhores estratégias e abertos ao constante aperfeiçoamento, desbravando teses e novas perspectivas em relação ao litígio. "

```html
<!DOCTYPE html>
<html lang="pt-BR">
<head>
<meta charset="utf-8">
<title>Ferraz &amp; Moreno — Blocos de Anotações</title>
<link rel="stylesheet" href="https://fonts.googleapis.com/css2?family=Cormorant+Garamond:wght@500;600&family=Montserrat:wght@400;500&display=swap">
<style>
  :root {
    --backdrop: #e9e4dc;
    --cover: #24272f;
    --paper: #fbfbfa;
    --gold: #c9a24a;
    --gold-deep: #a8812e;
    --ink: #3a3d44;
    --faint: #e4e5e7;
  }
  * { margin: 0; padding: 0; box-sizing: border-box; }
  html, body { width: 1200px; height: 1200px; overflow: hidden; }
  body {
    background: var(--backdrop);
    display: flex;
    align-items: center;
    justify-content: center;
    gap: 30px;
  }
  .pad {
    position: relative;
    width: 360px;
    height: 530px;
    overflow: hidden;
    box-shadow: 0 10px 24px rgba(0,0,0,.18);
  }
  .pad--cover { background: var(--cover); }
  .pad--letter, .pad--plain { background: var(--paper); }
  .pad--letter::after, .pad--plain::after {
    content: "";
    position: absolute;
    left: 0; right: 0; bottom: 0;
    height: 7px;
    background: linear-gradient(90deg, var(--gold-deep), var(--gold), var(--gold-deep));
  }

  .brand {
    position: absolute;
    top: 110px; left: 0; right: 0;
    text-align: center;
    color: var(--gold);
  }
  .brand__mark {
    display: block;
    width: 26px; height: 26px;
    margin: 0 auto 12px;
    background: var(--gold);
  }
  .brand__name {
    font-family: "Cormorant Garamond", serif;
    font-weight: 600;
    font-size: 25px;
    letter-spacing: 2px;
    text-transform: uppercase;
  }
  .brand__rule {
    width: 210px; height: 1px;
    margin: 6px auto 6px;
    background: var(--gold);
  }
  .brand__tagline {
    font-family: "Cormorant Garamond", serif;
    font-weight: 600;
    font-size: 10px;
    letter-spacing: 3.5px;
    text-transform: uppercase;
  }

  .cover-name {
    position: absolute;
    left: 18px;
    bottom: 46px;
    font-family: "Cormorant Garamond", serif;
    font-weight: 600;
    font-size: 78px;
    line-height: .9;
    color: var(--gold);
  }

  .watermark {
    position: absolute;
    top: 170px; left: 0; right: 0;
    text-align: center;
    font-family: "Cormorant Garamond", serif;
    font-weight: 600;
    font-size: 74px;
    line-height: .95;
    color: var(--faint);
  }

  .contact {
    position: absolute;
    left: 22px; right: 18px;
    bottom: 22px;
    display: flex;
    align-items: flex-start;
    gap: 18px;
    font-family: "Montserrat", sans-serif;
    font-size: 6.5px;
    line-height: 1.4;
    color: var(--ink);
  }
  .contact__item { display: flex; gap: 4px; align-items: flex-start; }
  .contact__icon { width: 8px; height: 8px; flex: none; fill: var(--gold); }
</style>
</head>
<body>

  <section class="pad pad--cover">
    <div class="brand">
      <span class="brand__mark"></span>
      <div class="brand__name">Ferraz &amp; Moreno</div>
      <div class="brand__rule"></div>
      <div class="brand__tagline">Sociedade de Advogados</div>
    </div>
    <div class="cover-name">Ferraz<br>&amp; Moreno</div>
  </section>

  <section class="pad pad--letter">
    <footer class="contact">
      <div class="contact__item">
        <svg class="contact__icon" viewBox="0 0 10 10"><path d="M2 0.5 L3.8 0.5 L4.4 3 L3.2 4 Q4.3 5.9 6 6.8 L7 5.6 L9.5 6.2 L9.5 8 Q9.5 9.5 8 9.5 Q1 8.8 0.5 2 Q0.5 0.5 2 0.5Z"/></svg>
        <span>+55 11 3000-0000</span>
      </div>
      <div class="contact__item">
        <svg class="contact__icon" viewBox="0 0 10 10"><path d="M0.5 2 H9.5 V8 H0.5Z M0.5 2 L5 5.5 L9.5 2" fill="none" stroke="#c9a24a" stroke-width="1"/></svg>
        <span>contato@ferrazmoreno.com.br</span>
      </div>
      <div class="contact__item">
        <svg class="contact__icon" viewBox="0 0 10 10"><path d="M5 0.5 A3.3 3.3 0 0 1 8.3 3.8 Q8.3 6 5 9.5 Q1.7 6 1.7 3.8 A3.3 3.3 0 0 1 5 0.5Z M5 2.6 A1.2 1.2 0 1 0 5 5 A1.2 1.2 0 1 0 5 2.6Z" fill-rule="evenodd"/></svg>
        <span>Rua das Acácias, 1200, Sala 4 · Centro<br>São Paulo – SP · CEP 01000-000</span>
      </div>
    </footer>
  </section>

  <section class="pad pad--plain">
    <div class="watermark">Ferraz<br>&amp;<br>Moreno</div>
  </section>

</body>
</html>
```